Emerging Australian photographer

I'm based in Cunderdin, a small rural town in the Wheatbelt area of Western Australia. So its a good thing that I love to travel further afield both for pleasure and for work. To me that is one and the same thing in any event!

My desire is to take photos that make the viewers heart skip. I love taking photos of people doing the things they love or being with the people they love. For me, the joy of photography comes with capturing the 'moments between the moments'. I like candid photography best of all - like when the new husband is staring joyfully at his bride and at that minute is unaware of the photographer capturing the moment.

I am available for weddings, engagements, birthdays, special events, newborns, family or individual portraits. By the end of the year I will be accredited with the Coastal Guild of Image Artisans.

I need a card that stands out but is elegant and would sit well on the table at a wedding or be given out in the church grounds. Classy and a little bit sassy.

Target Market(s)

Consumers who are seeking photographic services, eg wedding guests who see me at work and make enquiries.

Industry/Entity Type

Church

Contact Information for Business Card

Tamsin Bexley Photography
Tamsin Bexley
0452 307 618
www.tamsinbexley.com.au
photos@tamsinbexley.com.au

Requirements
Must have
• Must fit with the theme in the watermarks, but be crisp and modern.
Nice to have
• However it's not essential to have the pink! Facebook and Twitter logos.
Should not have
• Old style fonts like times new roman.

```html
<!DOCTYPE html>
<html lang="en">
<head>
<meta charset="utf-8">
<title>Tamsin Bexley Photography – Business Card</title>
<link rel="stylesheet" href="https://fonts.googleapis.com/css2?family=Sofia&family=Arimo:wght@400&display=swap">
<style>
  :root {
    --backdrop-light: #666666;
    --backdrop-dark: #3f3f3f;
    --card-white: #ffffff;
    --pink-deep: #f3a3c6;
    --pink-soft: #fbe3ed;
    --pink-name: #e0558f;
    --ink-grey: #666666;
    --contact-ink: #4a4a4a;
    --icon-pink: #ec5f9c;
  }
  html, body {
    margin: 0;
    padding: 0;
    width: 1200px;
    height: 1000px;
    overflow: hidden;
  }
  body {
    background: linear-gradient(180deg, var(--backdrop-light) 0%, var(--backdrop-dark) 100%);
    position: relative;
    font-family: "Arimo", Arial, sans-serif;
  }
  .card {
    position: absolute;
    top: 54px;
    width: 556px;
    height: 343px;
    background: var(--card-white);
    overflow: hidden;
    box-shadow: 0 2px 6px rgba(0,0,0,0.35);
  }
  .card--front { left: 30px; }
  .card--back { left: 615px; }
  .card__shape {
    position: absolute;
    inset: 0;
    width: 556px;
    height: 343px;
  }
  .front__name {
    position: absolute;
    left: 60px;
    top: 16px;
    margin: 0;
    font-family: "Sofia", cursive;
    font-weight: 400;
    font-size: 46px;
    line-height: 1.2;
    color: var(--pink-name);
    letter-spacing: 1px;
    white-space: nowrap;
  }
  .front__mark {
    position: absolute;
    left: 12px;
    top: 244px;
    width: 246px;
    display: flex;
    align-items: center;
    gap: 7px;
    font-family: "Sofia", cursive;
    font-size: 17px;
    line-height: 1;
    color: var(--card-white);
    white-space: nowrap;
  }
  .mark__dot {
    width: 10px;
    height: 10px;
    border-radius: 50%;
    background: var(--card-white);
    flex: none;
  }
  .contact-list {
    position: absolute;
    left: 278px;
    top: 196px;
    margin: 0;
    padding: 0;
    list-style: none;
  }
  .contact-list li {
    display: flex;
    align-items: center;
    height: 21px;
    font-size: 14px;
    color: var(--contact-ink);
    white-space: nowrap;
  }
  .contact-list svg {
    width: 12px;
    height: 12px;
    margin-right: 13px;
    flex: none;
  }
  .back__brand {
    position: absolute;
    left: 0;
    right: 0;
    top: 240px;
    display: flex;
    align-items: center;
    justify-content: center;
    gap: 12px;
    font-family: "Sofia", cursive;
    font-size: 38px;
    line-height: 1.2;
    color: var(--ink-grey);
    letter-spacing: 1px;
    white-space: nowrap;
  }
  .back__brand .mark__dot {
    width: 14px;
    height: 14px;
    background: var(--pink-deep);
  }
</style>
</head>
<body>

  <section class="card card--front" aria-label="Card front">
    <svg class="card__shape" viewBox="0 0 556 343" aria-hidden="true">
      <defs>
        <linearGradient id="front-pink" x1="0" y1="0" x2="1" y2="0">
          <stop offset="0" stop-color="#f3a3c6"/>
          <stop offset="1" stop-color="#fbe3ed"/>
        </linearGradient>
      </defs>
      <path d="M0,101 Q260,190 556,0 L556,343 L0,343 Z" fill="url(#front-pink)"/>
    </svg>

    <h1 class="front__name">tamsin bexley</h1>

    <div class="front__mark"><span class="mark__dot"></span>tamsin bexley photography</div>

    <ul class="contact-list">
      <li>
        <svg viewBox="0 0 12 12"><rect width="12" height="12" rx="2" fill="var(--icon-pink)"/><rect x="4" y="2.5" width="4" height="7" rx="0.8" fill="#fff"/></svg>
        0452 307 618
      </li>
      <li>
        <svg viewBox="0 0 12 12"><rect width="12" height="12" rx="2" fill="var(--icon-pink)"/><rect x="2.5" y="3.5" width="7" height="5" fill="#fff"/><path d="M2.5,3.5 L6,6.5 L9.5,3.5" fill="none" stroke="var(--icon-pink)" stroke-width="0.9"/></svg>
        photos@tamsinbexley.com.au
      </li>
      <li>
        <svg viewBox="0 0 12 12"><rect width="12" height="12" rx="2" fill="var(--icon-pink)"/><circle cx="6" cy="6" r="3.4" fill="none" stroke="#fff" stroke-width="1"/><path d="M2.6,6 H9.4 M6,2.6 V9.4" stroke="#fff" stroke-width="0.8"/></svg>
        www.tamsinbexley.com.au
      </li>
      <li>
        <svg viewBox="0 0 12 12"><rect width="12" height="12" rx="2" fill="var(--icon-pink)"/></svg>
        tamsinbexley.
      </li>
      <li>
        <svg viewBox="0 0 12 12"><rect width="12" height="12" rx="2" fill="var(--icon-pink)"/></svg>
        tamsinbexley.
      </li>
    </ul>
  </section>

  <section class="card card--back" aria-label="Card back">
    <svg class="card__shape" viewBox="0 0 556 343" aria-hidden="true">
      <defs>
        <linearGradient id="back-pink" x1="0" y1="0" x2="1" y2="0">
          <stop offset="0" stop-color="#fce6ef"/>
          <stop offset="1" stop-color="#f49cc3"/>
        </linearGradient>
      </defs>
      <path d="M25,0 Q300,255 556,100 L556,0 Z" fill="url(#back-pink)"/>
    </svg>

    <div class="back__brand"><span class="mark__dot"></span>tamsin bexley photography</div>
  </section>

</body>
</html>
```